Halvorn - Refresh the look and feel of an existing website

We currently have an existing website www.halvornworldadvisory.example however it needs a more refreshed 'look and feel'. We are a professional consultancy that works with large corporate organisations and government. Our 'tag line' is A New Way of Thinking. We want the site to communicate "Innovation" and Leading Edge Thinking.

Target Market(s)

Corporate and Professional Clients - Organisation and Business Change

Industry/Entity Type

Management Consulting

Number of Pages Required

1 page

Font styles to use
Sans Serif

Requirements
Must have
• Must have a professional Corporate look and feel. Header 'imagery' is ok but boxes on front page need changing ... along with the words. The focus on home page needs to 'call out' 3 main consulting areas:-
• - Change & Transformation Specialists
• - Innovative Solutions
• - Digital Transformation
• Tag Line for business is ... A New Way of Thinking (Highlighting Halvorn as 'Thought Leaders' in business)
Nice to have
• Less "words' more imagery. Possibly an area for a 'video' or recent articles/blogs on the front page. Needs to have more of an 'interactive' feel. We are open to suggestions.
Should not have
• NA

```html
<!DOCTYPE html>
<html lang="en">
<head>
<meta charset="utf-8">
<title>Halvorn Global Solutions</title>
<link rel="stylesheet" href="https://fonts.googleapis.com/css2?family=Questrial&family=Lato:wght@400;700&display=swap">
<style>
:root{
  --navy:#233a57;
  --navy-deep:#1d3049;
  --ink:#111;
  --text:#666;
  --green:#7aa12e;
  --pink:#b52b52;
  --teal:#15a1a5;
  --fb:#1f6fc4;
  --tw:#1ba5e6;
  --li:#1f4d69;
  --ig:#c91f35;
  --line:#cfd4da;
  --white:#fff;
}
*{box-sizing:border-box;margin:0;padding:0}
html,body{width:1200px;height:2594px;overflow:hidden}
body{position:relative;background:var(--white);font-family:'Lato',sans-serif;color:var(--text)}
.abs{position:absolute}
.heading{font-family:'Questrial',sans-serif}

/* header */
.site-header{left:0;top:0;width:1200px;height:118px;background:#f3f5f8}
.nav-link{top:40px;height:36px;line-height:36px;font-size:13px;color:#222;text-transform:uppercase;letter-spacing:.3px}
.nav-home{left:47px;width:88px;background:var(--navy);color:var(--white);text-align:center}
.nav-sep{top:48px;width:1px;height:18px;background:#444}
.brand{left:452px;top:28px;height:62px;display:flex;align-items:center;gap:14px}
.brand-dot{width:58px;height:58px;border-radius:50%;background:var(--navy)}
.brand-name{font-family:'Questrial',sans-serif;font-size:38px;color:var(--navy);letter-spacing:1px}

/* hero */
.hero{left:0;top:118px;width:1200px;height:720px;background:linear-gradient(180deg,#a9b6c2 0%,#cfd3cf 30%,#8aa96a 55%,#5c6a5e 80%,#4a5352 100%)}
.hero-title{left:0;top:398px;width:1200px;text-align:center;font-size:56px;color:var(--white);letter-spacing:1px;text-shadow:0 2px 6px rgba(0,0,0,.35)}

/* focus grid */
.tile{width:368px;height:252px;display:flex;align-items:center;justify-content:center;text-align:center;font-family:'Questrial',sans-serif;font-size:34px;line-height:1.05;color:var(--white);text-transform:uppercase}
.tile-green{background:var(--green)}
.tile-pink{background:var(--pink)}
.tile-teal{background:var(--teal)}
.tile-photo-tablet{background:linear-gradient(135deg,#cfe6f3,#6fb0d6 55%,#2d6e9a)}
.tile-photo-team{background:linear-gradient(180deg,#d9dde2,#8d949c 60%,#2d3540)}
.tile-photo-network{background:radial-gradient(circle at 55% 40%,#3d8ee0,#123a7a 55%,#061634)}
.chev{width:38px;height:38px;border-radius:50%;background:var(--white);display:flex;align-items:center;justify-content:center}

/* welcome */
.title-rule{height:1px;background:var(--line)}
.rule-dot{width:9px;height:9px;border:1px solid #999;border-radius:50%;background:var(--white)}
.welcome-title{left:0;top:1114px;width:1200px;text-align:center;font-size:35px;color:var(--ink)}
.welcome-title span{color:var(--navy)}
.welcome-text{left:120px;top:1180px;width:960px;text-align:center;font-size:12.5px;line-height:22px;color:#777}
.btn-more{left:526px;top:1274px;width:148px;height:45px;background:var(--navy);color:var(--white);font-size:13px;line-height:45px;text-align:center;text-transform:uppercase}

/* services */
.services{left:0;top:1371px;width:1200px;height:393px;background:radial-gradient(ellipse at 55% 45%,#3a4c63 0%,#1e2c3e 50%,#111b27 100%)}
.services-title{left:0;top:1412px;width:1200px;text-align:center;font-size:33px;color:var(--white)}
.service{width:520px;display:flex;gap:18px;align-items:flex-start}
.service-icon{flex:none;width:72px;height:72px;border-radius:50%;background:var(--white);display:flex;align-items:center;justify-content:center}
.service h3{font-size:17px;color:var(--white);font-weight:700;margin-top:8px;margin-bottom:4px}
.service p{font-size:13px;line-height:18px;color:#e3e7ec}
.view-all{left:1080px;top:1717px;font-size:12px;color:var(--white)}

/* follow */
.follow-title{left:0;top:1795px;width:1200px;text-align:center;font-size:29px;color:var(--ink)}
.follow-title span{color:var(--navy)}
.social{top:1871px;width:214px;height:48px;color:var(--white);font-weight:700;font-size:19px;display:flex;align-items:center;padding-left:22px;gap:30px}
.social i{display:block;width:12px;height:12px;background:var(--white)}
.social-count{top:1934px;width:214px;text-align:center;font-size:13px;color:#888}

/* get started */
.contact{left:0;top:1992px;width:1200px;height:524px;background:linear-gradient(135deg,#5b6454,#3d4a4c 40%,#4a5247 70%,#3a4244)}
.contact-shade{left:0;top:1992px;width:1200px;height:524px;background:rgba(20,28,36,.45)}
.contact-title{left:59px;top:2064px;font-size:29px;color:var(--white)}
.contact-intro{left:59px;top:2137px;width:470px;font-size:12px;line-height:20px;color:var(--white)}
.contact-sep{left:59px;top:2215px;width:470px;height:1px;background:rgba(255,255,255,.5)}
.contact-info{left:63px;top:2243px;font-size:14px;line-height:28px;color:var(--white);font-style:normal}
.field{left:664px;width:488px;border:1px solid rgba(255,255,255,.75);background:rgba(255,255,255,.08);color:var(--white);font-size:14px;padding:8px 12px}
.btn-send{left:1015px;top:2438px;width:137px;height:42px;background:var(--white);color:var(--navy);font-size:19px;line-height:42px;text-align:center;text-transform:uppercase}

/* footer */
.site-footer{left:0;top:2516px;width:1200px;height:78px;background:var(--navy-deep)}
.copyright{left:47px;top:2541px;font-size:12px;color:var(--white)}
.foot-icon{top:2538px;width:30px;height:30px;border:1px solid rgba(255,255,255,.7);display:flex;align-items:center;justify-content:center}
.foot-icon i{display:block;width:10px;height:10px;background:var(--white)}
</style>
</head>
<body>

<header class="abs site-header"></header>
<div class="abs nav-link nav-home">Home</div>
<div class="abs nav-link" style="left:170px">About Us</div>
<div class="abs nav-sep" style="left:265px"></div>
<div class="abs nav-link" style="left:295px">Our Services</div>
<div class="abs brand"><span class="brand-dot"></span><span class="brand-name">HALVORN</span></div>
<div class="abs nav-link" style="left:748px">Solutions</div>
<div class="abs nav-sep" style="left:852px"></div>
<div class="abs nav-link" style="left:882px">What's Happening</div>
<div class="abs nav-sep" style="left:1042px"></div>
<div class="abs nav-link" style="left:1072px">Contact Us</div>

<section class="abs hero" role="img" aria-label="Road rising into the sky as an arrow between green fields"></section>
<h1 class="abs hero-title heading">A New Way of Thinking</h1>

<div class="abs tile tile-green" style="left:47px;top:557px">Change &amp;<br>Transformation<br>Specialists</div>
<div class="abs tile tile-photo-tablet" style="left:416px;top:557px" role="img" aria-label="Hands using a tablet with a glowing globe and charts"></div>
<div class="abs tile tile-pink" style="left:785px;top:557px">Innovative<br>Solutions</div>
<div class="abs tile tile-photo-team" style="left:47px;top:811px" role="img" aria-label="Confident business team standing together"></div>
<div class="abs tile tile-teal" style="left:416px;top:811px">Digital<br>Transformation</div>
<div class="abs tile tile-photo-network" style="left:785px;top:811px" role="img" aria-label="Hand touching a glowing global network interface"></div>

<div class="abs chev" style="left:204px;top:790px"><svg width="14" height="9" viewBox="0 0 14 9"><path d="M1 1l6 6 6-6" fill="none" stroke="#222" stroke-width="2"/></svg></div>
<div class="abs chev" style="left:576px;top:790px"><svg width="14" height="9" viewBox="0 0 14 9"><path d="M1 8l6-6 6 6" fill="none" stroke="#222" stroke-width="2"/></svg></div>
<div class="abs chev" style="left:956px;top:790px"><svg width="14" height="9" viewBox="0 0 14 9"><path d="M1 1l6 6 6-6" fill="none" stroke="#222" stroke-width="2"/></svg></div>

<div class="abs title-rule" style="left:47px;top:1137px;width:230px"></div>
<div class="abs rule-dot" style="left:273px;top:1133px"></div>
<div class="abs title-rule" style="left:928px;top:1137px;width:225px"></div>
<div class="abs rule-dot" style="left:924px;top:1133px"></div>
<h2 class="abs welcome-title heading">Welcome to <span>Halvorn Global Solutions</span></h2>
<p class="abs welcome-text">Lorem ipsum dolor sit amet, consectetur adipiscing elit, sed do eiusmod tempor incididunt ut labore et dolore magna aliqua. Ut enim ad minim veniam, quis nostrud exercitation ullamco laboris nisi ut aliquip ex ea commodo consequat. Duis aute irure dolor in reprehenderit in voluptate velit esse cillum dolore eu fugiat nulla pariatur. Excepteur sint occaecat cupidatat non proident, sunt in culpa qui officia deserunt mollit anim id est laborum.</p>
<div class="abs btn-more">Read More</div>

<section class="abs services" role="img" aria-label="Businessman touching a digital interface on a dark background"></section>
<div class="abs title-rule" style="left:47px;top:1436px;width:435px;background:rgba(255,255,255,.55)"></div>
<div class="abs rule-dot" style="left:478px;top:1432px;background:transparent;border-color:#fff"></div>
<div class="abs title-rule" style="left:720px;top:1436px;width:433px;background:rgba(255,255,255,.55)"></div>
<div class="abs rule-dot" style="left:714px;top:1432px;background:transparent;border-color:#fff"></div>
<h2 class="abs services-title heading">Our&nbsp; Service</h2>

<div class="abs service" style="left:47px;top:1497px">
  <span class="service-icon"><svg width="26" height="26" viewBox="0 0 26 26"><circle cx="13" cy="8" r="5" fill="#233a57"/><path d="M3 25c0-6 4-10 10-10s10 4 10 10z" fill="#233a57"/></svg></span>
  <div><h3>Strategy and Design</h3><p>Lorem ipsum dolor sit amet, consectetur adipiscing elit, sed do eiusmod tempor incididunt ut labore et dolore magna aliqua. ➜</p></div>
</div>
<div class="abs service" style="left:641px;top:1497px">
  <span class="service-icon"><svg width="26" height="26" viewBox="0 0 26 26"><circle cx="13" cy="8" r="5" fill="#233a57"/><path d="M3 25c0-6 4-10 10-10s10 4 10 10z" fill="#233a57"/></svg></span>
  <div><h3>Project Management</h3><p>Lorem ipsum dolor sit amet, consectetur adipiscing elit, sed do eiusmod tempor incididunt ut labore et dolore magna aliqua. ➜</p></div>
</div>
<div class="abs service" style="left:47px;top:1593px">
  <span class="service-icon"><svg width="26" height="26" viewBox="0 0 26 26"><circle cx="13" cy="8" r="5" fill="#233a57"/><path d="M3 25c0-6 4-10 10-10s10 4 10 10z" fill="#233a57"/></svg></span>
  <div><h3>Organisational Development</h3><p>Lorem ipsum dolor sit amet, consectetur adipiscing elit, sed do eiusmod tempor incididunt ut labore et dolore magna aliqua. ➜</p></div>
</div>
<div class="abs service" style="left:641px;top:1593px">
  <span class="service-icon"><svg width="26" height="26" viewBox="0 0 26 26"><circle cx="13" cy="8" r="5" fill="#233a57"/><path d="M3 25c0-6 4-10 10-10s10 4 10 10z" fill="#233a57"/></svg></span>
  <div><h3>Organisational Efficiency</h3><p>Lorem ipsum dolor sit amet, consectetur adipiscing elit, sed do eiusmod tempor incididunt ut labore et dolore magna aliqua. ➜</p></div>
</div>
<div class="abs view-all">View All</div>

<div class="abs title-rule" style="left:47px;top:1814px;width:370px"></div>
<div class="abs rule-dot" style="left:413px;top:1810px"></div>
<div class="abs title-rule" style="left:810px;top:1814px;width:343px"></div>
<div class="abs rule-dot" style="left:806px;top:1810px"></div>
<h2 class="abs follow-title heading">Follow us to <span>Stay in Touch</span></h2>

<div class="abs social" style="left:90px;background:var(--fb)"><i></i>Kinfeed</div>
<div class="abs social" style="left:367px;background:var(--tw)"><i></i>Chirper</div>
<div class="abs social" style="left:640px;background:var(--li)"><i></i>Workline</div>
<div class="abs social" style="left:904px;background:var(--ig)"><i></i>Snapgram</div>
<div class="abs social-count" style="left:90px">1234 Like</div>
<div class="abs social-count" style="left:367px">1234 Followers</div>
<div class="abs social-count" style="left:640px">1234 Followers</div>
<div class="abs social-count" style="left:904px">1234 Followers</div>

<section class="abs contact" role="img" aria-label="Road map of a large country"></section>
<div class="abs contact-shade"></div>
<h2 class="abs contact-title heading">GET STARTED</h2>
<div class="abs title-rule" style="left:262px;top:2084px;width:890px;background:rgba(255,255,255,.6)"></div>
<div class="abs rule-dot" style="left:254px;top:2080px;background:transparent;border-color:#fff"></div>
<p class="abs contact-intro">Lorem ipsum dolor sit amet, consectetur adipiscing elit, sed do eiusmod tempor incididunt ut labore et dolore magna aliqua. Ut enim ad minim veniam, quis nostrud exercitation ullamco laboris nisi ut aliquip ex ea commodo consequat.</p>
<div class="abs contact-sep"></div>
<address class="abs contact-info">123 Address line1, Address line 2<br>Country, 123456.<br>Freephone: +1 234 567 890<br>Telephone: +1 234 567 890<br>FAX: +1 000 555 0199<br><br>E-mail: info@halvornworld.example</address>

<div class="abs field" style="top:2141px;height:34px">Name</div>
<div class="abs field" style="top:2208px;height:35px">Email id</div>
<div class="abs field" style="top:2274px;height:34px">Phone</div>
<div class="abs field" style="top:2334px;height:86px">Address</div>
<div class="abs btn-send">Send</div>

<footer class="abs site-footer"></footer>
<div class="abs copyright">Copyright 2016 Company Name. All Rights Reserved.</div>
<div class="abs foot-icon" style="left:1004px"><i></i></div>
<div class="abs foot-icon" style="left:1042px"><i></i></div>
<div class="abs foot-icon" style="left:1080px"><i></i></div>
<div class="abs foot-icon" style="left:1118px"><i></i></div>

</body>
</html>
```